New Custom Pizza Box Design Project For Independant Restaurant

We are looking for creative designs for our new custom printed pizza boxes. Designs should include the following:

-Our logo & company name
-A color scheme similar to our current logo
-Our physical and URL addresses & phone number (menu is attached)
-Ability to scale the design across several box sizes (10x10x2, 14x14x2, 18x13x2,
26x18x2)
- Any creative flair you think will make for the best design

Design can be on a white or kraft (tan) box.
Designs can be either two or three ink colors.

***Please note, designs must be able to be screen printed on boxes***
Updates

Reason: Still debating which to choose

Target Market(s)

Designs do not have to be targeted to any specific demographic.

Industry/Entity Type

Pizza Delivery

Font styles to use
Other font styles liked:
• Please use font similar to our logo text

Requirements
Must have
• -2 or 3 ink colors
• -company name, address, phone number, URL
• -company logo and colors
• -flexibility to use on different box sizes (10x10x2, 14x14x2, 18x13x2,
• 26x18x2)
• -utilize full printable area on boxes (including 2" dimension on box sides)
• ***Please note, designs must be able to be screen printed on boxes***
Should not have
• Design features with strong similarities to existing designs of other pizzerias

```html
<!DOCTYPE html>
<html lang="en">
<head>
<meta charset="utf-8">
<title>Marco's Lantern Pizzeria – Pizza Box Dieline</title>
<link rel="stylesheet" href="https://fonts.googleapis.com/css2?family=Pacifico&family=Yellowtail&family=Exo+2:wght@400;600;700&display=swap">
<style>
  :root {
    --backdrop: #d1d2d4;
    --brown: #7a4a33;
    --brown-light: #8d5a40;
    --yellow: #f2b922;
    --white: #ffffff;
  }
  html, body { margin: 0; padding: 0; overflow: hidden; }
  body {
    width: 1200px; height: 1200px;
    background: var(--backdrop);
    position: relative;
    font-family: "Exo 2", sans-serif;
  }
  .abs { position: absolute; }

  .lid-panel { left: 358px; top: 225px; width: 576px; height: 820px; background: var(--brown); }
  .side-flap { top: 347px; width: 115px; height: 575px; background: var(--yellow); box-shadow: inset 0 0 0 1px #b8891a; }
  .side-flap.left { left: 243px; }
  .side-flap.right { left: 934px; }

  .flap-text {
    position: absolute; top: 245px; height: 286px;
    writing-mode: vertical-rl; transform: rotate(180deg);
    font-size: 10.2px; line-height: 12.8px; letter-spacing: 0.2px;
    color: var(--brown); white-space: nowrap; margin: 0;
  }
  .side-flap.left .flap-text { left: 25px; }
  .side-flap.right .flap-text { left: 24px; }

  .flap-pizza-icon { position: absolute; left: 19px; top: 67px; width: 76px; height: 74px; }

  .name-label {
    border: 2px dashed var(--brown);
    outline: 4px solid var(--yellow);
    background: var(--yellow);
    display: flex; flex-direction: column; align-items: center; justify-content: center;
    color: var(--brown); font-family: "Pacifico", cursive; font-weight: 400;
    box-sizing: border-box; border-radius: 3px;
  }
  .name-label .sub {
    background: var(--brown);
    font-family: "Exo 2", sans-serif; font-weight: 700;
    text-align: center;
  }
  .name-label.small { width: 142px; height: 50px; font-size: 16px; line-height: 22px; }
  .name-label.small .sub { width: 66px; font-size: 9.5px; line-height: 12px; color: var(--yellow); letter-spacing: 0.5px; }
  .name-label.main { left: 459px; top: 504px; width: 373px; height: 132px; font-size: 46px; line-height: 66px; }
  .name-label.main .sub { width: 176px; font-size: 24px; line-height: 30px; color: var(--white); letter-spacing: 1.5px; margin-top: 2px; }

  .notice-script {
    width: 240px; text-align: center; color: var(--yellow);
    font-family: "Yellowtail", "Pacifico", cursive; font-size: 12.5px; line-height: 14px; margin: 0;
  }

  .name-mark {
    display: flex; flex-direction: column; align-items: center; gap: 4px;
    font-family: "Pacifico", cursive; text-align: center; line-height: 1.05;
  }
  .name-mark .dot { width: 10px; height: 10px; border-radius: 50%; }
  .name-mark.corner { width: 90px; font-size: 13px; color: var(--yellow); }
  .name-mark.corner .dot { background: var(--yellow); }
  .name-mark.center { left: 590px; top: 395px; width: 112px; font-size: 17px; color: var(--white); }
  .name-mark.center .dot { background: var(--white); }

  .deliver-heading { left: 758px; top: 800px; margin: 0; color: var(--yellow); font-family: "Yellowtail", "Pacifico", cursive; font-weight: 400; font-size: 32px; line-height: 40px; }
  .contact-block { left: 812px; top: 843px; border-left: 1px solid var(--white); padding-left: 7px; color: var(--white); font-style: normal; }
  .contact-block .phone { font-size: 13px; font-weight: 600; letter-spacing: 1.6px; line-height: 15px; }
  .contact-block .address { font-size: 6.4px; letter-spacing: 0.5px; line-height: 7.5px; text-transform: uppercase; margin-top: 2px; }
  .contact-block .web { font-size: 6.6px; letter-spacing: 0.8px; margin-top: 4px; }
</style>
</head>
<body>

  <section class="side-flap left abs">
    <svg class="flap-pizza-icon" viewBox="0 0 76 74" role="img" aria-label="Line drawing of a sliced pizza">
      <ellipse cx="38" cy="37" rx="37" ry="36" fill="#dea11e"/>
    </svg>
    <p class="flap-text">Prices do not include sales tax. Menu items and prices<br>are subject to change without notice.<br>A charge of $3.50 applies to all delivery orders, a por-<br>tion of which goes to the delivery driver.<br>Delivery times will vary and are not guaranteed.</p>
  </section>

  <section class="side-flap right abs">
    <svg class="flap-pizza-icon" viewBox="0 0 76 74" role="img" aria-label="Line drawing of a sliced pizza">
      <ellipse cx="38" cy="37" rx="37" ry="36" fill="#dea11e"/>
    </svg>
    <p class="flap-text">Prices do not include sales tax. Menu items and prices<br>are subject to change without notice.<br>A charge of $3.50 applies to all delivery orders, a por-<br>tion of which goes to the delivery driver.<br>Delivery times will vary and are not guaranteed.</p>
  </section>

  <main class="lid-panel abs"></main>

  <!-- top strip -->
  <div class="name-label small abs" style="left:393px; top:259px;">Marco's Lantern<span class="sub">Pizzeria</span></div>
  <p class="notice-script abs" style="left:560px; top:270px;">Prices do not include sales tax. Menu items and prices are subject to change without notice.</p>
  <div class="name-mark corner abs" style="left:810px; top:262px;"><span>Marco's Lantern</span><span class="dot"></span></div>

  <!-- checker areas -->
  <svg class="abs" style="left:788px; top:347px;" width="146" height="147" viewBox="0 0 146 147" role="img" aria-label="Stepped checkerboard pattern in yellow and brown">
    <polygon points="0,0 146,0 146,147" fill="var(--yellow)" opacity="0.6"/>
  </svg>
  <svg class="abs" style="left:358px; top:776px;" width="146" height="147" viewBox="0 0 146 147" role="img" aria-label="Stepped checkerboard pattern in yellow and brown">
    <polygon points="0,0 0,147 146,147" fill="var(--yellow)" opacity="0.6"/>
  </svg>

  <!-- pizza illustration area -->
  <svg class="abs" style="left:460px; top:500px;" width="350" height="400" viewBox="0 0 350 400" role="img" aria-label="White line drawing of a pizza with a slice lifted on a server">
    <circle cx="176" cy="176" r="164" fill="var(--brown-light)"/>
  </svg>

  <div class="name-mark center abs"><span>Marco's Lantern</span><span class="dot"></span></div>
  <div class="name-label main abs">Marco's Lantern<span class="sub">Pizzeria</span></div>

  <h2 class="deliver-heading abs">We Deliver!</h2>
  <address class="contact-block abs">
    <div class="phone">555-0142</div>
    <div class="address">1420 Harbor Avenue,<br>Westfield Plaza</div>
    <div class="web">marcoslantern.com</div>
  </address>

  <!-- bottom strip -->
  <div class="name-label small abs" style="left:393px; top:957px;">Marco's Lantern<span class="sub">Pizzeria</span></div>
  <p class="notice-script abs" style="left:560px; top:968px;">Prices do not include sales tax. Menu items and prices are subject to change without notice.</p>
  <div class="name-mark corner abs" style="left:810px; top:960px;"><span>Marco's Lantern</span><span class="dot"></span></div>

</body>
</html>
```